Whitening Flyer

I need an informational flyer for my dental practice. The flyer will describe the whitening services that are available at my practice and show price of each whitening service. We currently gave a 3 fold brochure, but I prefer something with a more professional look, and personalized with our branding and practice colors. I have attached the current flyer for you to use similar text. I will also attach a flyer that I have used in the past that could demonstrate my branding or feel free to view my website: www.grkvemu.com

```html
<!DOCTYPE html>
<html lang="en">
<head>
<meta charset="utf-8">
<title>Whitening Flyer</title>
<link href="https://fonts.googleapis.com/css2?family=Oswald:wght@500;700&family=Montserrat:wght@400;600;700&display=swap" rel="stylesheet">
<style>
:root{
  --red:#d71f27;
  --red-dark:#b3161d;
  --ink:#2b2b2b;
  --grey:#585858;
  --grey-light:#ededed;
  --grey-mid:#c9c9c9;
  --box:#efefef;
  --white:#ffffff;
  --gold-a:#f7e27a;
  --gold-b:#c9a227;
  --ice-a:#e3f0fa;
  --ice-b:#a8c9e4;
}
*{margin:0;padding:0;box-sizing:border-box}
html,body{width:900px;height:1200px;overflow:hidden;background:#f4f4f4}
body{font-family:"Montserrat",Arial,sans-serif;color:var(--ink)}
.flyer{position:relative;width:900px;height:1200px;background:var(--white);overflow:hidden}

.header{position:absolute;left:0;top:0;width:900px;height:490px}
.header-art{position:absolute;left:0;top:0}
.brand{position:absolute;left:40px;top:42px;display:flex;align-items:center;gap:12px}
.brand-dot{width:30px;height:30px;border-radius:50%;background:var(--red)}
.brand-name{font-family:"Montserrat",sans-serif;font-weight:700;font-size:32px;color:var(--red);letter-spacing:.5px}
.headline{position:absolute;left:40px;top:168px;font-family:"Oswald",sans-serif;font-weight:700;font-size:64px;line-height:70px;color:var(--red);letter-spacing:1px}

.start{position:absolute;left:38px;top:493px;width:830px}
.start h2{font-size:17px;font-weight:700;color:var(--red);letter-spacing:.5px}
.start p{font-size:11.5px;line-height:15px;margin-top:10px}
.factors{position:absolute;left:38px;top:562px;width:830px;display:flex;justify-content:space-between;list-style:none}
.factor{display:flex;align-items:center;gap:10px;font-size:16px;font-weight:600}
.factor-icon{width:30px;height:30px;border-radius:50%;background:var(--red);display:flex;align-items:center;justify-content:center}

.packages-title{position:absolute;left:0;width:900px;top:606px;text-align:center;font-family:"Montserrat",sans-serif;font-weight:700;font-size:32px;color:var(--red);letter-spacing:.5px}

.package{position:absolute;background:var(--box);border:1px solid var(--grey-mid);text-align:center}
.package .tag{position:absolute;left:50%;top:-10px;transform:translateX(-50%);height:46px;padding:6px 0 0;font-size:23px;font-weight:600;clip-path:polygon(0 0,100% 0,100% 78%,50% 100%,0 78%)}
.tag-basic{width:110px;background:linear-gradient(#555,#333);color:var(--white)}
.tag-silver{width:120px;background:linear-gradient(#f4f4f4,#9a9a9a 80%);color:var(--ink)}
.tag-gold{width:120px;background:linear-gradient(var(--gold-a),var(--gold-b));color:var(--ink)}
.tag-diamond{width:160px;background:linear-gradient(var(--ice-a),var(--ice-b));color:var(--ink)}
.tag-platinum{width:160px;background:linear-gradient(#fff,#cfcfcf);color:var(--ink)}
.price{margin-top:44px;font-family:"Oswald",sans-serif;font-weight:500;font-size:50px;line-height:54px;color:var(--red)}
.price sup{font-size:24px;vertical-align:top;position:relative;top:4px}
.rule{width:130px;height:2px;background:var(--ink);margin:4px auto 8px}
.desc{font-size:10px;line-height:12.5px;padding:0 16px}

.tagline{position:absolute;left:40px;top:1062px;width:804px;height:44px;border-radius:22px;background:var(--grey-mid);overflow:hidden;display:flex;align-items:center}
.tagline-lead{height:44px;width:395px;background:var(--red);color:var(--white);border-radius:22px;font-size:25px;font-weight:700;display:flex;align-items:center;padding-left:28px}
.tagline-rest{flex:1;text-align:center;font-size:25px;font-weight:700;color:var(--ink)}

.footer-band{position:absolute;left:0;top:1120px}
.contact{position:absolute;left:38px;top:1126px;color:var(--white)}
.phone{display:flex;align-items:center;gap:10px;font-size:24px;line-height:28px;font-weight:700}
.address{display:flex;align-items:flex-start;gap:10px;font-size:13px;font-weight:700;margin-top:5px;line-height:16px}
.address svg{flex:none;margin-top:1px}
.social{position:absolute;right:55px;top:1126px;display:flex;gap:22px}
.social span{width:26px;height:26px;border-radius:50%;background:#e15a5f}
.web{position:absolute;left:455px;top:1168px;width:400px;display:flex;justify-content:flex-end;align-items:center;gap:14px;font-size:14px;font-weight:700;color:var(--white)}
.web .sep{width:2px;height:18px;background:var(--white)}
.web-item{display:flex;align-items:center;gap:8px}
</style>
</head>
<body>
<main class="flyer">

  <section class="header">
    <svg class="header-art" width="900" height="490" viewBox="0 0 900 490">
      <defs>
        <linearGradient id="crowdTone" x1="0" y1="0" x2="1" y2="1">
          <stop offset="0" stop-color="#d9c1ab"/>
          <stop offset=".45" stop-color="#a9574a"/>
          <stop offset=".75" stop-color="#b8342f"/>
          <stop offset="1" stop-color="#6d8fbd"/>
        </linearGradient>
        <linearGradient id="headBg" x1="0" y1="0" x2="0" y2="1">
          <stop offset="0" stop-color="#fbfbfb"/>
          <stop offset="1" stop-color="#eeeeee"/>
        </linearGradient>
      </defs>
      <rect width="900" height="455" fill="url(#headBg)"/>
      <path d="M470 80 C 600 50, 760 40, 900 60 L900 430 C 800 440, 700 430, 610 420 C 520 410, 430 420, 400 430 Z" fill="url(#crowdTone)" role="img" aria-label="Group photo of smiling people of all ages"/>
      <path d="M0 428 C 160 430, 260 400, 420 392 C 560 386, 700 430, 900 420 L900 450 C 700 465, 560 412, 420 418 C 260 424, 150 450, 0 460 Z" fill="var(--red)"/>
      <path d="M0 460 C 150 450, 260 424, 420 418 C 560 412, 700 465, 900 450 L900 490 L0 490 Z" fill="var(--white)"/>
    </svg>
    <div class="brand"><span class="brand-dot"></span><span class="brand-name">Brightline Dental</span></div>
    <h1 class="headline">WHICH<br>WHITENING<br>IS RIGHT?</h1>
  </section>

  <section class="start">
    <h2>HOW DO YOU GET STARTED?</h2>
    <p>There are many options and factors to take into account when deciding which whitening option is best for you. Our team is here to help you in the deciding factors include;</p>
  </section>
  <ul class="factors">
    <li class="factor"><span class="factor-icon"><svg width="16" height="16" viewBox="0 0 16 16"><rect x="3" y="2" width="10" height="12" rx="2" fill="#fff"/></svg></span>The Cost</li>
    <li class="factor"><span class="factor-icon"><svg width="16" height="16" viewBox="0 0 16 16"><circle cx="8" cy="8" r="5" fill="#fff"/></svg></span>The Effort</li>
    <li class="factor"><span class="factor-icon"><svg width="16" height="16" viewBox="0 0 16 16"><path d="M3 3h10v5l-2 6-3-4-3 4-2-6z" fill="#fff"/></svg></span>The Sensitivity</li>
    <li class="factor"><span class="factor-icon"><svg width="16" height="16" viewBox="0 0 16 16"><path d="M3 8l3 3 7-7" stroke="#fff" stroke-width="2.5" fill="none"/></svg></span>The results:</li>
  </ul>

  <h2 class="packages-title">OUR WHITENING PACKAGES</h2>

  <article class="package" style="left:38px;top:668px;width:240px;height:184px">
    <div class="tag tag-basic">Basic</div>
    <div class="price"><sup>$</sup>10</div><div class="rule"></div>
    <p class="desc">One Upper and Lower one-time use 17 set and care instructions. No appointment needed</p>
  </article>
  <article class="package" style="left:291px;top:668px;width:240px;height:184px">
    <div class="tag tag-silver">Silver</div>
    <div class="price"><sup>$</sup>80</div><div class="rule"></div>
    <p class="desc">Ten Upper and lower one time use trays and care instructions. No appointment needed.</p>
  </article>
  <article class="package" style="left:544px;top:668px;width:298px;height:184px">
    <div class="tag tag-gold">Gold</div>
    <div class="price"><sup>$</sup>275</div><div class="rule"></div>
    <p class="desc">Custom made upper and lower whitening trays to be used at home. One 30 min office appointment for impressions. 4 tubes of professional whitening agent. At home care instructions (refills available for purchase of $35)</p>
  </article>
  <article class="package" style="left:145px;top:874px;width:290px;height:165px">
    <div class="tag tag-diamond">Diamond</div>
    <div class="price"><sup>$</sup>375</div><div class="rule"></div>
    <p class="desc">One 90 min office appointment for chairside Lumina whitening. At home care instructions.</p>
  </article>
  <article class="package" style="left:450px;top:874px;width:290px;height:165px">
    <div class="tag tag-platinum">Platinum</div>
    <div class="price"><sup>$</sup>475</div><div class="rule"></div>
    <p class="desc">One 2hr office appointment for chairside Lumina whitening. At home</p>
  </article>

  <div class="tagline">
    <span class="tagline-lead">At Brightline Dental</span>
    <span class="tagline-rest">we care about your smile</span>
  </div>

  <footer class="footer">
    <svg class="footer-band" width="900" height="80" viewBox="0 0 900 80">
      <rect x="380" y="38" width="520" height="42" fill="var(--grey)"/>
      <path d="M0 0 H390 L450 80 H0 Z" fill="var(--red)"/>
    </svg>
    <div class="contact">
      <div class="phone"><svg width="20" height="20" viewBox="0 0 20 20"><path d="M4 2l4 1 1 4-2 2c1 2 3 4 5 5l2-2 4 1 1 4-3 2C9 19 1 11 2 5z" fill="#fff"/></svg>(555)201-4837</div>
      <div class="address"><svg width="14" height="18" viewBox="0 0 16 20"><path d="M8 1a6 6 0 0 1 6 6c0 5-6 12-6 12S2 12 2 7a6 6 0 0 1 6-6z" fill="none" stroke="#fff" stroke-width="2"/><circle cx="8" cy="7" r="2" fill="#fff"/></svg><span>742 Harbor Ave, Lakeview,<br>ST, 00419</span></div>
    </div>
    <div class="social"><span></span><span></span></div>
    <div class="web">
      <span class="web-item"><svg width="16" height="12" viewBox="0 0 16 12"><rect width="16" height="12" fill="#fff"/><path d="M0 0l8 6 8-6" stroke="#585858" stroke-width="1.5" fill="none"/></svg>info@grkvemu.com</span>
      <span class="sep"></span>
      <span class="web-item"><svg width="15" height="15" viewBox="0 0 16 16"><circle cx="8" cy="8" r="7" fill="none" stroke="#fff" stroke-width="1.6"/><path d="M1 8h14M8 1c-3 4-3 10 0 14M8 1c3 4 3 10 0 14" stroke="#fff" stroke-width="1.2" fill="none"/></svg>www.grkvemu.com</span>
    </div>
  </footer>

</main>
</body>
</html>
```